Storm Restoration Contractor needs a professional business card design

Looking for a professional business card design. Not looking for your cheapo MS Word standard ones that are readily available. Dont want it to be cookie cutter look like ones readily available online. We just recently changed our logo and want to freshen up all our documents. Our company handles restoring a property back to a pre-loss condition after a storm damages it. For example, wind, hail, flood, fire losses.

Target Market(s)

Property Owners, Homeowners, Property Owners, Commercial Property Owners, Property Management Companies, Hail and Wind Damaged Properties

Industry/Entity Type

Construction Company

Contact Information for Business Card

Brightline Facades
847-555-0193
847-555-0147 fax
www.brightlinefacades.example
info@brightlinefacades.example

Requirements
Must have
• Clean, Professional, fresh look
• Storm Restoration, Roofing, Siding, Windows
Nice to have
• If there is a way to incorporate storms that may be cool.

```html
<!DOCTYPE html>
<html lang="en">
<head>
<meta charset="utf-8">
<title>Brightline Facades — Business Card</title>
<link rel="stylesheet" href="https://fonts.googleapis.com/css2?family=Michroma&family=Open+Sans:wght@400;600;700&display=swap">
<style>
  :root {
    --backdrop: #141414;
    --card-white: #ffffff;
    --brand-blue: #1b78c8;
    --brand-blue-light: #2186d8;
    --ink: #1e1e1e;
    --on-blue: #ffffff;
  }
  html, body {
    margin: 0;
    padding: 0;
    width: 1200px;
    height: 900px;
    overflow: hidden;
    background: var(--backdrop);
  }
  .canvas {
    position: relative;
    width: 1200px;
    height: 900px;
  }
  .card {
    position: absolute;
    top: 170px;
    width: 347px;
    height: 561px;
    box-shadow: 0 6px 18px rgba(0,0,0,0.55);
  }
  .card--front { left: 259px; }
  .card--back  { left: 631px; }
  .card svg { display: block; }
  .person-name {
    font-family: "Michroma", sans-serif;
    font-size: 17px;
    fill: var(--brand-blue);
    letter-spacing: 1px;
  }
  .body-text {
    font-family: "Open Sans", sans-serif;
    font-size: 14px;
    fill: var(--ink);
  }
  .label { fill: var(--brand-blue); font-weight: 700; }
  .website {
    font-family: "Open Sans", sans-serif;
    font-size: 14px;
    font-weight: 700;
    fill: var(--brand-blue);
  }
  .brand-name {
    font-family: "Open Sans", sans-serif;
    font-weight: 700;
  }
  .brand-name--front { font-size: 22px; fill: var(--brand-blue); }
  .brand-name--back  { font-size: 38px; fill: var(--on-blue); letter-spacing: 1px; }
  .service {
    font-family: "Open Sans", sans-serif;
    font-size: 26px;
    fill: var(--on-blue);
  }
</style>
</head>
<body>
<div class="canvas">

  <div class="card card--front">
    <svg width="347" height="561" viewBox="0 0 347 561">
      <rect class="card-face" width="347" height="561" fill="var(--card-white)"/>
      <path class="tab tab--top" d="M102 0 H245 V40 Q173.5 18 102 40 Z" fill="var(--brand-blue)"/>
      <path class="tab tab--bottom" d="M102 561 H245 V521 Q173.5 543 102 521 Z" fill="var(--brand-blue)"/>

      <g class="brand-lockup">
        <circle cx="173.5" cy="140" r="16" fill="var(--brand-blue)"/>
        <text class="brand-name brand-name--front" x="173.5" y="190" text-anchor="middle">BRIGHTLINE FACADES</text>
      </g>

      <text class="person-name" x="173.5" y="357" text-anchor="middle">DANIEL MERCER</text>
      <text class="body-text" x="173.5" y="377" text-anchor="middle">Managing Director</text>

      <text class="body-text" x="173.5" y="414" text-anchor="middle"><tspan class="label">P:</tspan> 847-555-0193</text>
      <text class="body-text" x="173.5" y="434" text-anchor="middle"><tspan class="label">F:</tspan> 847-555-0147</text>
      <text class="body-text" x="173.5" y="454" text-anchor="middle"><tspan class="label">E:</tspan> info@brightlinefacades.example</text>

      <text class="website" x="173.5" y="492" text-anchor="middle">www.brightlinefacades.example</text>
    </svg>
  </div>

  <div class="card card--back">
    <svg width="347" height="561" viewBox="0 0 347 561">
      <rect class="card-face" width="347" height="561" fill="var(--brand-blue)"/>
      <circle class="backdrop-ring" cx="173.5" cy="300" r="245" fill="none" stroke="var(--brand-blue-light)" stroke-width="40"/>

      <g class="brand-lockup">
        <circle cx="173.5" cy="167" r="46" fill="none" stroke="var(--on-blue)" stroke-width="8"/>
        <text class="brand-name brand-name--back" x="173.5" y="282" text-anchor="middle">BRIGHTLINE</text>
        <text class="brand-name brand-name--back" x="173.5" y="324" text-anchor="middle">FACADES</text>
      </g>

      <g class="services">
        <text class="service" x="173.5" y="414" text-anchor="middle">Storm Restoration</text>
        <text class="service" x="173.5" y="449" text-anchor="middle">Roofing</text>
        <text class="service" x="173.5" y="485" text-anchor="middle">Siding</text>
        <text class="service" x="173.5" y="521" text-anchor="middle">Windows</text>
      </g>
    </svg>
  </div>

</div>
</body>
</html>
```